Business Card Design for Kidvale (Hires out childrens play areas)

Looking to have a business card designed for a company we just bought. The company rents out childrens play areas.

I have uploaded a couple of examples of the kind of business card style I like. Here are two more examples:

https://quorvastudio.nz/project/bright-romp-branding/
https://imgvaultcdn.com/design_img/8841052/302917/302917_5518203_8841052_b73e19a2_image.jpg

I think a white card will be best due to all the colours in the logo.

Size we require: 3.75" x 2.25" (horizontally orientated) with a 0.125" bleed

Uploaded is two versions of our logo.

Details for the card:
1. My name: Liam Verster
2. Title: Managing Director
3. Phone no: 021 563 417
4. Email: liam@kidvale.co.nz
5. URL: www.kidvale.co.nz
6. Address:
PO Box 318625
Fernlea, Auckland

Let me know if you need anything else.

Target Market(s)

Hospitals, doctors surgeries, bed shops, etc.

Contact Information for Business Card

Details for the card:
1. My name: Liam Verster
3. Phone no: 021 563 417
5. URL: www.kidvale.co.nz
6. Address:
PO Box 318625
Fernlea, Auckland

Requirements
Should not have
• Not too busy.

```html
<!DOCTYPE html>
<html lang="en">
<head>
<meta charset="utf-8">
<title>Kidvale Business Card – Liam Verster</title>
<link rel="stylesheet" href="https://fonts.googleapis.com/css2?family=Merriweather+Sans:wght@700&family=Roboto:wght@400&display=swap">
<style>
  :root {
    --page-bg: #e9e7e4;
    --card-bg: #ffffff;
    --name-blue: #1d5676;
    --text-dark: #3a3a3a;
    --icon-blue: #2a5472;
    --brand-purple: #8a2fb0;
    --brand-magenta: #d0268f;
    --brand-violet: #6a34b4;
  }
  html, body {
    margin: 0;
    padding: 0;
    width: 1200px;
    height: 1054px;
    overflow: hidden;
    background: var(--page-bg);
  }
  .business-card {
    position: absolute;
    left: 100px;
    top: 227px;
    width: 1000px;
    height: 600px;
    background: var(--card-bg);
    overflow: hidden;
    box-shadow: 0 6px 24px rgba(0,0,0,0.12);
    font-family: "Roboto", Arial, sans-serif;
  }
  .holder-name {
    position: absolute;
    left: 51px;
    top: 58px;
    margin: 0;
    font-family: "Merriweather Sans", "Trebuchet MS", sans-serif;
    font-weight: 700;
    font-size: 36px;
    color: var(--name-blue);
    line-height: 1;
  }
  .holder-title {
    position: absolute;
    left: 51px;
    top: 110px;
    margin: 0;
    font-size: 26px;
    color: var(--text-dark);
    line-height: 1;
  }
  .brand-name {
    position: absolute;
    left: 640px;
    top: 140px;
    display: flex;
    align-items: center;
    gap: 16px;
    font-family: "Merriweather Sans", "Trebuchet MS", sans-serif;
    font-weight: 700;
    font-size: 62px;
    color: var(--brand-violet);
    line-height: 1;
  }
  .brand-dot {
    width: 34px;
    height: 34px;
    border-radius: 50%;
    background: var(--brand-magenta);
  }
  .contact-list {
    position: absolute;
    left: 62px;
    top: 394px;
    margin: 0;
    padding: 0;
    list-style: none;
  }
  .contact-item {
    display: flex;
    align-items: center;
    height: 37px;
    font-size: 24px;
    color: var(--text-dark);
  }
  .contact-icon {
    width: 20px;
    height: 20px;
    margin-right: 18px;
    fill: var(--icon-blue);
  }
  .postal-address {
    position: absolute;
    left: 51px;
    top: 512px;
    margin: 0;
    font-size: 24px;
    color: var(--text-dark);
    font-style: normal;
  }
  .character-side {
    position: absolute;
    left: 0;
    top: 165px;
    width: 127px;
    height: 230px;
    border-radius: 0 115px 115px 0;
    background: linear-gradient(135deg, var(--brand-purple), var(--brand-magenta));
    opacity: 0.85;
  }
  .character-corner {
    position: absolute;
    left: 591px;
    top: 340px;
    width: 409px;
    height: 260px;
    border-radius: 200px 0 0 0;
    background: linear-gradient(120deg, var(--brand-violet), var(--brand-purple) 50%, var(--brand-magenta));
  }
</style>
</head>
<body>
  <div class="business-card">
    <div class="character-side" role="img" aria-label="Cropped cartoon child character illustration peeking in from the left edge"></div>
    <div class="character-corner" role="img" aria-label="Large cartoon child character illustration rising from the bottom right corner"></div>

    <h1 class="holder-name">Liam Verster</h1>
    <p class="holder-title">Managing Director</p>

    <div class="brand-name"><span class="brand-dot"></span>Kidvale</div>

    <ul class="contact-list">
      <li class="contact-item">
        <svg class="contact-icon" viewBox="0 0 24 24" aria-hidden="true"><path d="M3 8c0-2 2-4 9-4s9 2 9 4v2h-5V8H8v2H3V8zm3 4h12l2 8H4l2-8zm6 1.5a3 3 0 1 0 0 6 3 3 0 0 0 0-6z"/></svg>
        021 563 417
      </li>
      <li class="contact-item">
        <svg class="contact-icon" viewBox="0 0 24 24" aria-hidden="true"><path d="M2 5h20v14H2V5zm2 2v.5l8 5.5 8-5.5V7l-8 5.5L4 7z"/></svg>
        liam@kidvale.co.nz
      </li>
      <li class="contact-item">
        <svg class="contact-icon" viewBox="0 0 24 24" aria-hidden="true"><path d="M12 2a10 10 0 1 0 0 20 10 10 0 0 0 0-20zm6.9 9h-3a15 15 0 0 0-1.4-6A8 8 0 0 1 18.9 11zM12 4.1c.9 1.3 1.7 3.6 1.9 6.9h-3.8c.2-3.3 1-5.6 1.9-6.9zM9.5 5a15 15 0 0 0-1.4 6h-3A8 8 0 0 1 9.5 5zm-4.4 8h3a15 15 0 0 0 1.4 6A8 8 0 0 1 5.1 13zm6.9 6.9c-.9-1.3-1.7-3.6-1.9-6.9h3.8c-.2 3.3-1 5.6-1.9 6.9zm2.5-.9a15 15 0 0 0 1.4-6h3a8 8 0 0 1-4.4 6z"/></svg>
        www.kidvale.co.nz
      </li>
    </ul>

    <address class="postal-address">PO Box 318625 Fernlea, Auckland</address>
  </div>
</body>
</html>
```